Quietly Orchard Honey Labels

We are an importer and distributor in the UK of fine foods from Spain. We sell primarily to the retail and wholesale trade. I need a design for wrap around labels to put on jars for four different varieties of honey - Creamy Spring Blossom, Lavender, Wild Forest and Wild Thyme. The honey originates from Spain and will primarily be sold online and to independent retailers. The look and feeling I am looking for is classical, traditional, artisan and natural. I am looking for something simple and not too fussy. There needs to be an immediate obvious distinction on each label between the 4 varieties of honey, ideally by the use of different colours in some way in each design, though I would prefer the label background to be predominantly white. It is not necessary in the design to make it evident that it is from Spain. I have attached images of the jars and the honeys and also an image of the current label just for reference (but do not refer to the design). I have also attached the text for each variety of honey. The measurements for the labels are as follows: 167mm wide and 82mm high. Our logo will go on top of the lid of the jar. I really like the design I have attached to my brief. It is labelled 'Honey Design'.

Target Market(s)

Independent food retailers and online consumers

Industry/Entity Type

Fine Foods

Font styles to use
Script
Other font styles liked:
• Freeland Font for the word Honey

Requirements
Must have
• It needs to be immediately obvious by sight that each of the 4 varieties of honey are different
Nice to have
• Just the one same icon on each label for each variety of honey. Simple. Not too fussy. I really like the design attached labelled 'honey font'.

```html
<!DOCTYPE html>
<html lang="en">
<head>
<meta charset="utf-8">
<title>Quietly Orchard Honey Labels</title>
<link rel="stylesheet" href="https://fonts.googleapis.com/css2?family=Figtree:wght@700;800;900&family=Crimson+Pro:wght@400;600&family=Mulish:wght@400;800&display=swap">
<style>
  :root {
    --page: #f4f3f1;
    --paper: #fbfbfa;
    --ink: #2b2b2b;
    --ink-soft: #555;
    --lavender-deep: #8e4f9c;
    --lavender-light: #d9a6d6;
    --blossom-deep: #e58fba;
    --blossom-light: #f3c6dc;
    --thyme-deep: #2e9e49;
    --thyme-light: #8fd08f;
    --forest-deep: #e9a422;
    --forest-light: #f2dc4a;
  }
  * { box-sizing: border-box; margin: 0; padding: 0; }
  html, body { width: 1118px; height: 1200px; overflow: hidden; background: var(--page); }
  .sheet { position: relative; width: 1118px; height: 1200px; }

  .label {
    position: absolute; width: 520px; height: 255px;
    background: var(--paper);
    box-shadow: 0 2px 10px rgba(0,0,0,.12);
    color: var(--ink); overflow: hidden;
  }
  .label--lavender { left: 29px;  top: 220px; --deep: var(--lavender-deep); --light: var(--lavender-light); }
  .label--blossom  { left: 569px; top: 220px; --deep: var(--blossom-deep);  --light: var(--blossom-light); }
  .label--thyme    { left: 29px;  top: 785px; --deep: var(--thyme-deep);    --light: var(--thyme-light); }
  .label--forest   { left: 569px; top: 785px; --deep: var(--forest-deep);   --light: var(--forest-light); }

  .label__art { position: absolute; inset: 0; }

  .nutrition {
    position: absolute; left: 14px; top: 40px; height: 140px;
    display: flex; gap: 6px;
    font-family: "Mulish", sans-serif; font-size: 6.5px; color: var(--ink-soft);
  }
  .nutrition__col {
    writing-mode: vertical-rl; transform: rotate(180deg);
    display: flex; justify-content: space-between; line-height: 1.25;
    border-right: 0.6px solid #999; padding-left: 3px;
  }
  .nutrition__col--values { justify-content: flex-end; gap: 12px; }
  .nutrition__col--dates { justify-content: flex-end; border: 0; margin-left: 10px; }

  .spanish-name {
    position: absolute; left: 226px; top: 24px; width: 58px;
    font-family: "Crimson Pro", serif; font-size: 7.5px; line-height: 1.1;
    text-align: right; color: var(--ink);
  }
  .net-weight {
    position: absolute; left: 150px; top: 205px;
    font-family: "Crimson Pro", serif; font-size: 7.5px; line-height: 1.1;
  }

  .variety-name {
    position: absolute; font-family: "Figtree", sans-serif; font-weight: 900;
    color: var(--ink); line-height: .95; letter-spacing: -0.3px;
  }
  .variety-name span { display: block; }

  .bee-illustration {
    position: absolute; left: 232px; top: 128px; width: 92px; height: 92px;
    border-radius: 46% 46% 40% 40%;
    background: radial-gradient(ellipse at 50% 55%, rgba(40,40,40,.55), color-mix(in srgb, var(--deep) 35%, transparent) 65%, transparent 72%);
  }

  .story {
    position: absolute; left: 322px; top: 38px; width: 184px;
    font-family: "Crimson Pro", serif; font-size: 8.4px; line-height: 1.55;
    text-align: justify; color: var(--ink);
  }
  .story mark {
    background: color-mix(in srgb, var(--deep) 55%, transparent);
    color: color-mix(in srgb, var(--deep) 55%, #222);
    padding: 0 1px;
  }
  .brand {
    position: absolute; left: 322px; top: 172px; width: 184px; text-align: right;
    font-family: "Mulish", sans-serif; font-weight: 800; font-size: 7px; letter-spacing: .6px;
  }
  .contact {
    position: absolute; left: 322px; top: 188px; width: 184px; text-align: right;
    font-family: "Mulish", sans-serif; font-size: 6px; line-height: 1.9; color: var(--ink-soft);
  }
</style>
</head>
<body>
<main class="sheet">

  <!-- Lavender -->
  <section class="label label--lavender">
    <svg class="label__art" viewBox="0 0 520 255" width="520" height="255" aria-hidden="true">
      <defs>
        <linearGradient id="lav-top" x1="0" y1="0" x2="1" y2="1"><stop offset="0" stop-color="var(--lavender-deep)"/><stop offset="1" stop-color="var(--lavender-light)"/></linearGradient>
        <linearGradient id="lav-bottom" x1="0" y1="0" x2="1" y2="1"><stop offset="0" stop-color="var(--lavender-deep)"/><stop offset="1" stop-color="var(--lavender-light)"/></linearGradient>
      </defs>
      <rect class="frame" x="140" y="16" width="150" height="224" fill="none" stroke="#2b2b2b" stroke-width="1.6"/>
      <polygon points="205,27 255.2,56 255.2,114 205,143 154.8,114 154.8,56" fill="url(#lav-top)"/>
      <polygon points="252,120 302.2,149 302.2,207 252,236 201.8,207 201.8,149" fill="url(#lav-bottom)"/>
    </svg>
    <div class="nutrition">
      <div class="nutrition__col"><span>Of which sugar</span><span>Protein</span><span>Salt</span></div>
      <div class="nutrition__col nutrition__col--values"><span>80.6g</span><span>&lt;0.5g</span><span>0.017g</span></div>
      <div class="nutrition__col nutrition__col--dates"><span>Best before:</span><span>Batch No.:</span></div>
    </div>
    <p class="spanish-name">miel<br>de<br>lavanda</p>
    <h2 class="variety-name" style="left:124px;top:54px;font-size:23px;"><span>Lavender</span><span style="font-size:32px;padding-left:30px;">Honey</span></h2>
    <div class="bee-illustration" role="img" aria-label="Engraved honeybee illustration tinted lavender"></div>
    <p class="net-weight">Net<br>weight:<br>xxx g</p>
    <p class="story">Three generations of family beekeepers go into producing this floral scented lavender honey on a traditional apiary nestled in the wild highlands of <mark>Aragón, Spain.</mark> <mark>Master beekeeper Tomás Ferrera and his family</mark> carefully nurture and manage over 3000 hives of healthy honeybees to produce all natural honey at its very best.</p>
    <p class="brand">QUIETLY ORCHARD</p>
    <p class="contact">Lower Brampton, Hollis<br>sales@quietlyorchard.example</p>
  </section>

  <!-- Creamy Spring Blossom -->
  <section class="label label--blossom">
    <svg class="label__art" viewBox="0 0 520 255" width="520" height="255" aria-hidden="true">
      <defs>
        <linearGradient id="blo-top" x1="0" y1="0" x2="1" y2="1"><stop offset="0" stop-color="var(--blossom-deep)"/><stop offset="1" stop-color="var(--blossom-light)"/></linearGradient>
        <linearGradient id="blo-bottom" x1="0" y1="0" x2="1" y2="1"><stop offset="0" stop-color="var(--blossom-deep)"/><stop offset="1" stop-color="var(--blossom-light)"/></linearGradient>
      </defs>
      <rect class="frame" x="140" y="16" width="150" height="224" fill="none" stroke="#2b2b2b" stroke-width="1.6"/>
      <polygon points="205,27 255.2,56 255.2,114 205,143 154.8,114 154.8,56" fill="url(#blo-top)"/>
      <polygon points="252,120 302.2,149 302.2,207 252,236 201.8,207 201.8,149" fill="url(#blo-bottom)"/>
    </svg>
    <div class="nutrition">
      <div class="nutrition__col"><span>Of which sugar</span><span>Protein</span><span>Salt</span></div>
      <div class="nutrition__col nutrition__col--values"><span>80.6g</span><span>&lt;0.5g</span><span>0.017g</span></div>
      <div class="nutrition__col nutrition__col--dates"><span>Best before:</span><span>Batch No.:</span></div>
    </div>
    <p class="spanish-name">flor de<br>primavera<br>cremoso</p>
    <h2 class="variety-name" style="left:112px;top:46px;font-size:22px;text-align:center;width:172px;"><span>Creamy</span><span style="font-size:18px;padding:3px 0;">Spring Blossom</span><span style="font-size:23px;padding-left:26px;">Honey</span></h2>
    <div class="bee-illustration" role="img" aria-label="Engraved honeybee illustration tinted pink"></div>
    <p class="net-weight">Net<br>weight:<br>xxx g</p>
    <p class="story">Three generations of family beekeepers go into producing this creamy, multi floral spring blossom honey on a traditional apiary nestled in the wild highlands of Aragón, Spain. <mark>Master beekeeper Tomás Ferrera and his family</mark> carefully nurture and manage over 3000 hives of healthy honeybees to produce all natural honey at its very best.</p>
    <p class="brand">QUIETLY ORCHARD</p>
    <p class="contact">Lower Brampton, Hollis<br>sales@quietlyorchard.example</p>
  </section>

  <!-- Wild Thyme -->
  <section class="label label--thyme">
    <svg class="label__art" viewBox="0 0 520 255" width="520" height="255" aria-hidden="true">
      <defs>
        <linearGradient id="thy-top" x1="0" y1="0" x2="1" y2="1"><stop offset="0" stop-color="var(--thyme-deep)"/><stop offset="1" stop-color="var(--thyme-light)"/></linearGradient>
        <linearGradient id="thy-bottom" x1="0" y1="0" x2="1" y2="1"><stop offset="0" stop-color="var(--thyme-deep)"/><stop offset="1" stop-color="var(--thyme-light)"/></linearGradient>
      </defs>
      <rect class="frame" x="140" y="16" width="150" height="224" fill="none" stroke="#2b2b2b" stroke-width="1.6"/>
      <polygon points="205,27 255.2,56 255.2,114 205,143 154.8,114 154.8,56" fill="url(#thy-top)"/>
      <polygon points="252,120 302.2,149 302.2,207 252,236 201.8,207 201.8,149" fill="url(#thy-bottom)"/>
    </svg>
    <div class="nutrition">
      <div class="nutrition__col"><span>Of which sugar</span><span>Protein</span><span>Salt</span></div>
      <div class="nutrition__col nutrition__col--values"><span>80.6g</span><span>&lt;0.5g</span><span>0.017g</span></div>
      <div class="nutrition__col nutrition__col--dates"><span>Best before:</span><span>Batch No.:</span></div>
    </div>
    <p class="spanish-name">miel de<br>tomillo<br>silvestre</p>
    <h2 class="variety-name" style="left:120px;top:40px;font-size:30px;"><span style="padding-left:6px;">Wild</span><span>Thyme</span><span style="padding-left:22px;">Honey</span></h2>
    <div class="bee-illustration" role="img" aria-label="Engraved honeybee illustration tinted green"></div>
    <p class="net-weight">Net<br>weight:<br>xxx g</p>
    <p class="story">Three generations of family beekeepers go into producing this wild thyme honey on a traditional apiary nestled in the wild highlands of <mark>Aragón, Spain.</mark> <mark>Master beekeeper Tomás Ferrera and his family</mark> carefully nurture and manage over 3000 hives of healthy honeybees to produce all natural honey at its very best.</p>
    <p class="brand">QUIETLY ORCHARD</p>
    <p class="contact">Lower Brampton, Hollis<br>sales@quietlyorchard.example</p>
  </section>

  <!-- Wild Forest -->
  <section class="label label--forest">
    <svg class="label__art" viewBox="0 0 520 255" width="520" height="255" aria-hidden="true">
      <defs>
        <linearGradient id="for-top" x1="0" y1="0" x2="1" y2="1"><stop offset="0" stop-color="var(--forest-deep)"/><stop offset="1" stop-color="var(--forest-light)"/></linearGradient>
        <linearGradient id="for-bottom" x1="0" y1="0" x2="1" y2="1"><stop offset="0" stop-color="var(--forest-deep)"/><stop offset="1" stop-color="var(--forest-light)"/></linearGradient>
      </defs>
      <rect class="frame" x="140" y="16" width="150" height="224" fill="none" stroke="#2b2b2b" stroke-width="1.6"/>
      <polygon points="205,27 255.2,56 255.2,114 205,143 154.8,114 154.8,56" fill="url(#for-top)"/>
      <polygon points="252,120 302.2,149 302.2,207 252,236 201.8,207 201.8,149" fill="url(#for-bottom)"/>
    </svg>
    <div class="nutrition">
      <div class="nutrition__col"><span>Of which sugar</span><span>Protein</span><span>Salt</span></div>
      <div class="nutrition__col nutrition__col--values"><span>80.6g</span><span>&lt;0.5g</span><span>0.017g</span></div>
      <div class="nutrition__col nutrition__col--dates"><span>Best before:</span><span>Batch No.:</span></div>
    </div>
    <p class="spanish-name">miel<br>de<br>bosque<br>salvaje</p>
    <h2 class="variety-name" style="left:124px;top:40px;font-size:30px;"><span style="padding-left:6px;">Wild</span><span>Forest</span><span style="padding-left:22px;">Honey</span></h2>
    <div class="bee-illustration" role="img" aria-label="Engraved honeybee illustration tinted golden yellow"></div>
    <p class="net-weight">Net<br>weight:<br>xxx g</p>
    <p class="story">Three generations of family beekeepers go into producing this wild forest honey on a traditional apiary nestled in the wild highlands of <mark>Aragón, Spain.</mark> <mark>Master beekeeper Tomás Ferrera and his family</mark> carefully nurture and manage over 3000 hives of healthy honeybees to produce all natural honey at its very best.</p>
    <p class="brand">QUIETLY ORCHARD</p>
    <p class="contact">Lower Brampton, Hollis<br>sales@quietlyorchard.example</p>
  </section>

</main>
</body>
</html>
```